kestrova business cards

Hey design gurus!
I'm after a clean, modern, stylish business card for my about to be launched company.
I've uploaded the logos for my company "Kestrova Electrical Solutions"
and also the tarrow alliance logo to whom i am associated.

```html
<!DOCTYPE html>
<html lang="en">
<head>
<meta charset="utf-8">
<title>Kestrova Electrical Solutions — Business Cards</title>
<link rel="stylesheet" href="https://fonts.googleapis.com/css2?family=Open+Sans:wght@400;600;700;800&display=swap">
<style>
  :root {
    --stage: #232323;
    --brand-blue: #2591d1;
    --brand-blue-deep: #1a6ea6;
    --ink: #111111;
    --paper: #ffffff;
    --badge-line: #a65a4a;
    --badge-navy: #1c2a4f;
    --icon-blue: #2a8fd0;
  }
  * { box-sizing: border-box; margin: 0; padding: 0; }
  html, body { width: 1200px; height: 780px; overflow: hidden; }
  body {
    background: var(--stage);
    font-family: "Open Sans", Arial, sans-serif;
    display: flex;
    flex-direction: column;
    align-items: center;
    justify-content: center;
    gap: 40px;
  }
  .card {
    width: 560px;
    height: 320px;
    position: relative;
    overflow: hidden;
    box-shadow: 0 12px 30px rgba(0,0,0,.55);
  }

  /* Front */
  .card--front {
    background: var(--brand-blue);
    display: flex;
    align-items: center;
    justify-content: center;
  }
  .wordmark {
    display: flex;
    align-items: center;
    gap: 14px;
    font-weight: 800;
    letter-spacing: .04em;
    text-transform: uppercase;
  }
  .wordmark__dot {
    border-radius: 50%;
    flex: none;
  }
  .card--front .wordmark { color: var(--brand-blue-deep); font-size: 24px; }
  .card--front .wordmark__dot {
    width: 58px; height: 58px;
    border: 4px solid var(--brand-blue-deep);
  }

  /* Back */
  .card--back { background: var(--paper); }
  .card--back .wordmark {
    position: absolute;
    left: 34px; top: 34px;
    color: var(--brand-blue);
    font-size: 16px;
    gap: 10px;
  }
  .card--back .wordmark__dot {
    width: 40px; height: 40px;
    border: 3px solid var(--brand-blue);
  }

  .address {
    position: absolute;
    left: 44px; top: 150px;
    font-size: 14px;
    line-height: 1.4;
    color: var(--ink);
  }
  .contacts {
    position: absolute;
    left: 44px; top: 222px;
    list-style: none;
    font-size: 14px;
    line-height: 1.55;
    color: var(--ink);
  }
  .contacts li { display: flex; align-items: center; gap: 8px; }
  .contacts svg { width: 13px; height: 13px; flex: none; }

  .person {
    position: absolute;
    right: 34px; top: 96px;
    text-align: right;
  }
  .person__name {
    font-size: 26px;
    font-weight: 700;
    color: var(--ink);
    line-height: 1.1;
  }
  .person__name .first { color: var(--brand-blue); }
  .person__role {
    font-size: 14px;
    color: var(--ink);
    margin-top: 2px;
  }
  .edge-tab {
    position: absolute;
    right: 0; top: 92px;
    width: 18px; height: 56px;
    background: var(--brand-blue);
  }

  .alliance-badge {
    position: absolute;
    right: 34px; top: 196px;
    width: 178px; height: 62px;
    border: 1.5px solid var(--badge-line);
    border-radius: 8px;
    display: flex;
    align-items: center;
    padding-left: 12px;
  }
  .alliance-badge__mark {
    width: 40px; height: 40px;
    background: var(--badge-navy);
    border-radius: 4px;
  }
</style>
</head>
<body>

  <section class="card card--front" aria-label="Business card front">
    <div class="wordmark">
      <span class="wordmark__dot" aria-hidden="true"></span>
      <span>Kestrova Electrical Solutions</span>
    </div>
  </section>

  <section class="card card--back" aria-label="Business card back">
    <div class="wordmark">
      <span class="wordmark__dot" aria-hidden="true"></span>
      <span>Kestrova Electrical Solutions</span>
    </div>

    <p class="address">4180 Meadowbrook Ave. Suite 120<br>Arlington, TX 76010</p>

    <ul class="contacts">
      <li>
        <svg viewBox="0 0 16 16" aria-hidden="true"><path fill="var(--icon-blue)" d="M3.6 1.5l2.3 2.6-1.3 1.8c.9 2 2.5 3.6 4.5 4.5l1.8-1.3 2.6 2.3-1.2 2.1C7 13.3 2.7 9 1.5 2.7z"/></svg>
        (555) 214-6083
      </li>
      <li>
        <svg viewBox="0 0 16 16" aria-hidden="true"><rect x="1" y="3" width="14" height="10" rx="1.5" fill="var(--icon-blue)"/><path d="M1.5 4l6.5 5 6.5-5" fill="none" stroke="#fff" stroke-width="1.3"/></svg>
        info@kestrovaelectric.com
      </li>
      <li>
        <svg viewBox="0 0 16 16" aria-hidden="true"><circle cx="8" cy="8" r="7" fill="var(--icon-blue)"/><path d="M1 8h14M8 1c-3 3.5-3 10.5 0 14M8 1c3 3.5 3 10.5 0 14" fill="none" stroke="#fff" stroke-width="1"/></svg>
        www.kestrovaelectric.com
      </li>
    </ul>

    <span class="edge-tab" aria-hidden="true"></span>
    <div class="person">
      <p class="person__name"><span class="first">Lenka</span> Horvath</p>
      <p class="person__role">Managing Director</p>
    </div>

    <div class="alliance-badge" role="img" aria-label="Tarrow Alliance partner badge">
      <span class="alliance-badge__mark"></span>
    </div>
  </section>

</body>
</html>
```